Finch Haulage Ltd

We need an A5 size (UK size) flyer to advertise our new business which is called Finch Haulage.
Domestic and Commercial Waste Clearance Services.
Please have the question in bold "Do you have a pile of junk you need to dispose of?"
We collect all kinds of junk or rubbish from homes and businesses across Kent, Sussex and South London.
No fuss, no mess!
A low cost, hassle free alternative to skip hire.
Licensed by the Landcare Board and fully insured (this can be in small print at the bottom).
Please put the Recycle symbol somewhere.
Our tagline on our vehicle is "We Clear More, For Less!"
We'd like the flyer to be bold and eye-catching (to catch the eye of the homeowner or business owner while it's sitting on their doormat).
We need our telephone, website and email to be prominent. Maybe saying "Call today for a free quote"
Tel. 01734 586019
Email: info@finchhaulage.example.co.uk
www.finchhaulage.example.co.uk
Target Market(s)
Our market will be homes and small businesses around Kent, Sussex and South London.

```html
<!DOCTYPE html>
<html lang="en">
<head>
<meta charset="utf-8">
<title>Finch Haulage – Waste Clearance Flyer</title>
<link rel="stylesheet" href="https://fonts.googleapis.com/css2?family=Arimo:wght@400;700&family=Montserrat:wght@700&display=swap">
<style>
  :root {
    --brand-grey: #58585a;
    --logo-grey: #4d4d4f;
    --headline-yellow: #ffff00;
    --eco-green: #22ae57;
    --contact-green: #4caf5c;
    --paper: #ffffff;
    --small-print: #555555;
  }
  * { margin: 0; padding: 0; box-sizing: border-box; }
  html, body { width: 846px; height: 1200px; overflow: hidden; background: var(--paper); }
  .flyer {
    position: relative;
    width: 846px;
    height: 1200px;
    font-family: "Arimo", Arial, sans-serif;
    background: var(--paper);
  }
  .brand {
    position: absolute;
    top: 0; left: 0; width: 100%; height: 238px;
    display: flex; align-items: center; justify-content: center;
  }
  .brand-name {
    font-family: "Montserrat", Arial, sans-serif;
    font-weight: 700;
    font-size: 62px;
    color: var(--logo-grey);
    letter-spacing: 1px;
  }
  .headline-band {
    position: absolute;
    top: 238px; left: 0; width: 100%; height: 267px;
    background: var(--brand-grey);
    display: flex; align-items: center; justify-content: center;
  }
  .headline {
    color: var(--headline-yellow);
    font-weight: 700;
    font-size: 73px;
    line-height: 70px;
    text-align: center;
    margin-top: -4px;
  }
  .pitch {
    position: absolute;
    top: 520px; left: 0; width: 100%;
    text-align: center;
    color: var(--eco-green);
    font-size: 42px;
    line-height: 46px;
  }
  .pitch strong { font-weight: 700; }
  .bin {
    position: absolute;
    top: 730px; left: 284px;
    width: 292px; height: 400px;
  }
  .contact {
    position: absolute;
    left: 18px; top: 890px;
    color: var(--contact-green);
    font-weight: 700;
  }
  .contact .tel { font-size: 29px; line-height: 36px; }
  .contact .web, .contact .email { font-size: 16.5px; line-height: 22px; margin-top: 12px; }
  .contact .web { margin-top: 14px; }
  .cta {
    position: absolute;
    left: 574px; top: 858px;
    color: var(--eco-green);
    font-weight: 700;
    font-size: 40px;
    line-height: 58px;
  }
  .licence {
    position: absolute;
    bottom: 12px; left: 0; width: 100%;
    text-align: center;
    color: var(--small-print);
    font-weight: 700;
    font-size: 19px;
  }
</style>
</head>
<body>
<main class="flyer">
  <header class="brand">
    <span class="brand-name">Finch Haulage</span>
  </header>

  <section class="headline-band">
    <h1 class="headline">Do you have a pile<br>of junk you need<br>to dispose of?</h1>
  </section>

  <p class="pitch">
    We collect all kinds of junk or rubbish<br>
    from homes and business.<br>
    <strong>No fuss, no mess!</strong><br>
    Very competitive prices.
  </p>

  <svg class="bin" viewBox="0 0 292 400" role="img" aria-label="Green recycling bin with recycle symbol">
    <rect x="98" y="2" width="96" height="40" rx="20" fill="var(--eco-green)"/>
    <path d="M2 84 Q2 38 60 38 L232 38 Q290 38 290 84 Z" fill="var(--eco-green)"/>
    <path d="M22 96 L268 96 L268 360 Q268 398 230 398 L60 398 Q22 398 22 360 Z" fill="var(--eco-green)"/>
    <circle cx="148" cy="234" r="108" fill="var(--paper)"/>
    <g transform="translate(148 240)" fill="var(--eco-green)">
      <g id="recycle-arrow">
        <path d="M-52 36 L14 36 L14 24 L46 47 L14 70 L14 58 L-52 58 Z"/>
      </g>
      <use href="#recycle-arrow" transform="rotate(120)"/>
      <use href="#recycle-arrow" transform="rotate(240)"/>
    </g>
  </svg>

  <address class="contact" style="font-style:normal">
    <div class="tel">Tel. 01734 586019</div>
    <div class="web">www.finchhaulage.example.co.uk</div>
    <div class="email">info@finchhaulage.example.co.uk</div>
  </address>

  <p class="cta">Call today<br>for a free<br>quote</p>

  <p class="licence">Licensed by the Landcare Board and fully insured.</p>
</main>
</body>
</html>
```